Cancer ppt courses for healthcare pro

We are organizing a contest for designers to modernize and improve an existing PowerPoint presentation titled "Along the Quiet Shore of Healing Days." This presentation is aimed at healthcare professionals, patients, and the general public, to inform them about the treatment and remission journey of breast cancer.
Objective
The goal of the contest is to create a visually appealing, clear, and professional PowerPoint presentation while maintaining the accuracy and precision of the medical information.
Requirements
Visual Design
Create a modern and consistent design for the entire presentation.
Use a soothing and professional color palette.
Integrate relevant visuals (icons, illustrations, photos) to support the content.
Ensure good readability with clear and appropriate fonts.
Structure and Organization
Maintain the logical and sequential structure of the existing content.
Reorganize information to improve clarity and flow if necessary.
Add smooth transitions between sections to facilitate understanding.
Thrilled
Preserve the integrity and accuracy of the medical information.
Highlight key points and important statistics.
Use charts and tables to present data visually and comprehensibly.
Updates
Faible participation designers
Target Market(s)
physiotherapist
Requirements
Must have
- it its new way of elarning courses, this presentation will be mixed with interviews, documentars... more like a movie

```html
<!DOCTYPE html>
<html lang="en">
<head>
<meta charset="utf-8">
<title>Along the Quiet Shore of Healing Days – Slide Overview</title>
<link href="https://fonts.googleapis.com/css2?family=Montserrat:wght@400;500;600;700;800;900&family=Playfair+Display:wght@700;900&display=swap" rel="stylesheet">
<style>
:root{
  --pink:#d9749a;
  --pink-soft:#e9a3bd;
  --lavender:#ecdbea;
  --lilac:#d9c3d6;
  --ink:#1b1b1b;
  --grey:#8a8a8a;
  --page:#d7d8da;
  --paper:#ffffff;
}
*{margin:0;padding:0;box-sizing:border-box}
html,body{width:815px;height:1200px;overflow:hidden;background:var(--page)}
body{position:relative;font-family:"Montserrat",sans-serif;color:var(--ink)}
.slide{position:absolute;width:237.5px;height:134px;background:var(--paper);overflow:hidden;box-shadow:0 1px 3px rgba(0,0,0,.18)}
.c1{left:41px}.c2{left:288.5px}.c3{left:536px}
.r1{top:36px}.r2{top:178px}.r3{top:321px}.r4{top:462px}.r5{top:604px}.r6{top:746px}.r7{top:888px}.r8{top:1029px}
.abs{position:absolute}
.brand{position:absolute;right:6px;top:6px;display:flex;align-items:center;gap:2px;font:600 3.6px/1 "Montserrat",sans-serif;color:var(--pink)}
.brand i{display:block;width:3.6px;height:3.6px;background:var(--pink)}
.foot-line{position:absolute;left:12px;right:6px;bottom:7px;height:.4px;background:var(--pink)}
.foot-mark{position:absolute;left:5px;bottom:5px;width:4px;height:4px;background:var(--pink)}
.page-no{position:absolute;right:4px;bottom:3px;font-size:2.4px;color:var(--ink)}
.title{position:absolute;left:11px;top:11px;font:600 7.2px/1.15 "Montserrat",sans-serif;color:var(--ink)}
.rule{position:absolute;left:11px;top:23px;width:12px;height:.8px;background:var(--pink)}
.fill{font:400 2.3px/1.35 "Montserrat",sans-serif;color:var(--grey)}
.fill-pink{font:400 2.3px/1.35 "Montserrat",sans-serif;color:var(--pink)}
.h-pink{font:600 3.6px/1.2 "Montserrat",sans-serif;color:var(--pink)}
.h-ink{font:700 3.6px/1.2 "Montserrat",sans-serif;color:var(--ink)}
.photo{position:absolute}
.serif{font-family:"Playfair Display",serif}
.center{text-align:center}
.dot-num{position:absolute;width:11px;height:11px;border-radius:50%;background:var(--pink);color:#fff;font:700 5px/11px "Montserrat",sans-serif;text-align:center}
</style>
</head>
<body>

<!-- 1 cover A -->
<section class="slide c1 r1">
  <div class="abs" style="left:5px;top:5px;width:6px;height:6px;background:var(--ink)"></div>
  <div class="abs" style="left:229px;top:0;width:8.5px;height:124px;background:var(--ink)"></div>
  <div class="abs" style="left:103px;top:119px;width:134.5px;height:15px;background:var(--pink)"></div>
  <div class="abs" style="left:18px;top:21px;display:flex;align-items:center;gap:3px;font:600 7px/1 Montserrat,sans-serif;color:var(--pink)"><i style="display:block;width:7px;height:7px;background:var(--pink)"></i>Tidewell Physio</div>
  <p class="abs" style="left:18px;top:50px;width:70px;font:600 3.4px/1.2 Montserrat,sans-serif">Physiotherapy care for women</p>
  <p class="abs" style="left:18px;top:62px;width:90px;font:700 9px/1.1 Montserrat,sans-serif;color:var(--pink)">Along the Quiet<br>Shore of <span style="color:var(--ink)">Healing Days</span></p>
  <p class="abs" style="left:18px;top:106px;width:70px;font:italic 400 2.5px/1.35 Montserrat,sans-serif">Élise Marchand<br>Breast-care physiotherapist<br>Harbourside Clinic</p>
  <div class="abs" style="left:152px;top:35px;width:14px;height:4px;border-top:1px dotted var(--pink)"></div>
  <div class="photo" role="img" aria-label="Photo of a woman in a pink top holding a pink ribbon" style="left:119px;top:13px;width:105px;height:108px;background:linear-gradient(160deg,#f1eeee,#e7c6cf 55%,#d06a8e)"></div>
</section>

<!-- 2 cover B -->
<section class="slide c2 r1">
  <div class="photo" role="img" aria-label="Photo of a smiling woman in a pink sweater holding a pink ribbon" style="left:100px;top:0;width:137.5px;height:108px;background:linear-gradient(150deg,#ead7e6,#e8c3cf 60%,#d99cb0)"></div>
  <div class="abs" style="left:16px;top:13px;display:flex;align-items:center;gap:3px;font:600 7px/1 Montserrat,sans-serif;color:var(--pink)"><i style="display:block;width:7px;height:7px;background:var(--pink)"></i>Tidewell Physio</div>
  <p class="abs" style="left:16px;top:42px;width:70px;font:600 3.4px/1.2 Montserrat,sans-serif">Physiotherapy care for women</p>
  <p class="abs" style="left:16px;top:54px;width:82px;font:700 9px/1.1 Montserrat,sans-serif;color:var(--pink)">Along the Quiet<br>Shore of <span style="color:var(--ink)">Healing Days</span></p>
  <p class="abs" style="left:16px;top:98px;width:70px;font:italic 400 2.5px/1.35 Montserrat,sans-serif">Élise Marchand<br>Breast-care physiotherapist<br>Harbourside Clinic</p>
  <div class="abs" style="left:16px;top:120px;display:flex;gap:2px"><i style="width:2px;height:2px;border-radius:50%;background:var(--ink)"></i><i style="width:2px;height:2px;border-radius:50%;background:var(--pink)"></i><i style="width:2px;height:2px;border-radius:50%;background:var(--ink)"></i></div>
  <p class="abs" style="left:138px;top:119px;font:400 3.4px/1 Montserrat,sans-serif;letter-spacing:1.2px;color:var(--pink)">www.website.com</p>
</section>

<!-- 3 agenda -->
<section class="slide c3 r1">
  <div class="brand"><i></i>Tidewell</div>
  <div class="abs" style="left:65px;top:27px;width:129px;height:81px;background:var(--lavender)"></div>
  <div class="abs" style="left:33px;top:56px;width:58px;height:26px;background:var(--pink);color:#fff;font:700 9px/26px Montserrat,sans-serif;text-align:center">Agenda</div>
  <div class="abs" style="left:38px;top:52px;width:3px;height:6px;background:var(--ink)"></div>
  <div class="abs" style="left:78px;top:79px;width:3px;height:6px;background:var(--ink)"></div>
  <div class="abs" style="left:102px;top:35px;width:82px">
    <p class="h-ink" style="font-size:3.2px;font-weight:600">1. Lorem ipsum</p><p class="fill-pink" style="margin-bottom:9px">Short note on the opening topic<br>of the course session</p>
    <p class="h-ink" style="font-size:3.2px;font-weight:600">2. Lorem ipsum</p><p class="fill-pink" style="margin-bottom:9px">Short note on the second topic<br>of the course session</p>
    <p class="h-ink" style="font-size:3.2px;font-weight:600">3. Lorem ipsum</p><p class="fill-pink" style="margin-bottom:9px">Short note on the third topic<br>of the course session</p>
    <p class="h-ink" style="font-size:3.2px;font-weight:600">4. Lorem ipsum</p><p class="fill-pink">Short note on the closing topic<br>of the course session</p>
  </div>
  <div class="foot-mark"></div><div class="foot-line"></div><span class="page-no">2</span>
</section>

<!-- 4 text with painting -->
<section class="slide c1 r2">
  <div class="brand"><i></i>Tidewell</div>
  <div class="abs" style="left:0;top:10px;width:2px;height:14px;background:var(--pink)"></div>
  <h2 class="title" style="top:12px">Text<br>Added Here</h2>
  <div class="rule" style="top:31px"></div>
  <p class="fill abs" style="left:11px;top:38px;width:58px">Gentle care after surgery helps the body recover its range, ease and trust in each small daily move.<br><br>Guided sessions follow each patient through every stage of treatment and return to calm routines.<br><br>Each exercise is shaped to her pace, her scars and her goals, with clear support from the team.</p>
  <div class="photo" role="img" aria-label="Classical painting of reclining figures" style="left:82px;top:21px;width:155.5px;height:90px;background:linear-gradient(135deg,#5a4030,#a78068 50%,#3b2a22)"></div>
  <div class="abs" style="left:112px;top:66px;width:40px;height:50px;background:#fff;box-shadow:0 .5px 1.5px rgba(0,0,0,.2)"><div style="height:14px;background:var(--pink);color:#fff;font:600 5px/14px Montserrat,sans-serif;text-align:center">Text Here</div><p class="fill" style="padding:2px 3px;font-size:1.9px">Brief note on this stage of care and what it brings to daily life.</p></div>
  <div class="abs" style="left:164px;top:66px;width:40px;height:50px;background:#fff;box-shadow:0 .5px 1.5px rgba(0,0,0,.2)"><div style="height:14px;background:var(--pink);color:#fff;font:600 5px/14px Montserrat,sans-serif;text-align:center">Text Here</div><p class="fill" style="padding:2px 3px;font-size:1.9px">Brief note on this stage of care and what it brings to daily life.</p></div>
  <div class="foot-mark"></div><div class="foot-line"></div><span class="page-no">3</span>
</section>

<!-- 5 three linked boxes -->
<section class="slide c2 r2">
  <div class="brand"><i></i>Tidewell</div>
  <h2 class="title">Text Added Here</h2><div class="rule"></div>
  <div class="photo" role="img" aria-label="Faint world map background" style="left:38px;top:28px;width:160px;height:70px;background:radial-gradient(ellipse at center,#ececec,#fafafa 70%)"></div>
  <svg class="abs" style="left:0;top:0" width="237.5" height="134" viewBox="0 0 237.5 134" fill="none" stroke="#1b1b1b" stroke-width="1.3">
    <rect x="47" y="36" width="38" height="58" rx="3"/>
    <rect x="100" y="36" width="38" height="58" rx="3"/>
    <rect x="151" y="36" width="38" height="58" rx="3"/>
    <path d="M85 60 H92 V70 H100" /><path d="M138 60 H145 V70 H151"/>
    <circle cx="92" cy="60" r="1.5" fill="#1b1b1b"/><circle cx="145" cy="70" r="1.5" fill="#1b1b1b"/>
    <circle cx="66" cy="42" r="3" stroke="#d9749a" stroke-width=".7"/><circle cx="119" cy="42" r="3" stroke="#d9749a" stroke-width=".7"/><circle cx="170" cy="42" r="3" stroke="#d9749a" stroke-width=".7"/>
  </svg>
  <div class="abs center" style="left:49px;top:47px;width:34px"><p class="h-pink" style="font-size:2.6px">LOREM IPSUM</p><p class="fill" style="font-size:1.9px">Short summary of the first key idea for this part</p></div>
  <div class="abs center" style="left:102px;top:47px;width:34px"><p class="h-pink" style="font-size:2.6px">LOREM IPSUM</p><p class="fill" style="font-size:1.9px">Short summary of the second key idea for this part</p></div>
  <div class="abs center" style="left:153px;top:47px;width:34px"><p class="h-pink" style="font-size:2.6px">LOREM IPSUM</p><p class="fill" style="font-size:1.9px">Short summary of the third key idea for this part</p></div>
  <p class="fill abs center" style="left:30px;top:103px;width:178px;color:#555">Each step of the pathway builds on the last, from the first visit to the final review of progress and comfort.</p>
  <div class="foot-mark"></div><div class="foot-line"></div><span class="page-no">4</span>
</section>

<!-- 6 numbered paragraphs -->
<section class="slide c3 r2">
  <div class="brand"><i></i>Tidewell</div>
  <h2 class="title">Text Added Here</h2><div class="rule"></div>
  <div class="abs" style="left:20px;top:31px;width:205px">
    <p class="h-pink" style="font-size:3.4px;font-weight:500">1. Text Added Here</p>
    <p class="fill" style="margin-bottom:8px">The first phase covers the diagnosis, the plan of care and the early steps to keep the shoulder and chest moving freely. Short daily routines reduce tension, support the lymph flow and help the patient feel in charge of her own recovery at home and in clinic.</p>
    <p class="h-pink" style="font-size:3.4px;font-weight:500">2. Text Added Here</p>
    <p class="fill" style="margin-bottom:8px">The second phase follows surgery and treatment, with scar care, breathing work and gentle strength. Sessions adapt to fatigue, pain and mood, and each gain is noted so progress stays visible for the patient and for the wider care team.</p>
    <p class="h-pink" style="font-size:3.4px;font-weight:500">3. Text Added Here</p>
    <p class="fill">The final phase looks at remission, return to work and sport, and the long view of body image. Patients leave with a simple plan they can keep, and clear signs that tell them when to come back for a check.</p>
  </div>
  <div class="foot-mark"></div><div class="foot-line"></div><span class="page-no">5</span>
</section>

<!-- 7 subject title -->
<section class="slide c1 r3">
  <div class="brand"><i></i>Tidewell</div>
  <div class="abs" style="left:0;top:10px;width:2px;height:14px;background:var(--pink)"></div>
  <h2 class="title" style="top:10px">Subject<br>Title</h2>
  <div class="rule" style="left:11px;top:38px"></div>
  <p class="fill abs" style="left:11px;top:48px;width:52px">Soft tissue work around the scar keeps the skin supple and helps limit pulling at the chest wall. It is started once the wound has closed and grows slowly with each visit, always within a level of comfort the patient agrees to.</p>
  <div class="photo" role="img" aria-label="Renaissance portrait painting of a woman" style="left:69px;top:0;width:44px;height:83px;background:linear-gradient(160deg,#2f2620,#8d6a52 55%,#3d2e24)"></div>
  <div class="abs" style="left:113px;top:34px;width:124.5px;height:72px;background:var(--lavender)"></div>
  <div class="photo" role="img" aria-label="Clinical photo of a post-surgery breast scar" style="left:120px;top:42px;width:47px;height:76px;background:linear-gradient(150deg,#c9b9b3,#b88a90 55%,#a8838a)"></div>
  <p class="abs serif" style="left:173px;top:45px;width:60px;font-weight:700;font-size:5.4px;line-height:1.25">Lorem Ipsum<br>Dolor Sit<br>Ametkeeper.</p>
  <p class="fill-pink abs" style="left:173px;top:74px;width:48px;color:#fff">Gentle skin work<br>around the scar<br>line each week<br><br>helps keep tissue<br>soft and free</p>
  <div class="foot-mark"></div><div class="foot-line"></div><span class="page-no">6</span>
</section>

<!-- 8 section break -->
<section class="slide c2 r3" style="background:var(--lilac)">
  <div class="abs" style="left:10px;top:9px;width:218px;height:116px;background:#fff"></div>
  <div class="photo" role="img" aria-label="Illustration of a large pink awareness ribbon" style="left:12px;top:18px;width:48px;height:106px;background:linear-gradient(160deg,#f3c6d4,#e296b0 60%,#f7e3ea);border-radius:22px 22px 4px 4px"></div>
  <div class="photo" role="img" aria-label="Illustration of a pink ribbon loop with petals" style="left:172px;top:12px;width:56px;height:58px;background:linear-gradient(200deg,#ea9fb8,#f6dbe4);border-radius:50% 40% 40% 50%"></div>
  <div class="photo" role="img" aria-label="Illustration of falling pink petals" style="left:175px;top:92px;width:46px;height:28px;background:radial-gradient(ellipse,#f3c9d6,#fff 70%)"></div>
  <p class="abs serif center" style="left:50px;top:50px;width:140px;font-weight:700;font-size:13px;color:var(--ink)">Section Break</p>
  <p class="abs center" style="left:50px;top:73px;width:140px;font:400 4px/1.2 Montserrat,sans-serif;color:#9a9a9a">Lorem ipsum dolor sit amet, consectetuer adipiscing elit sed diam nonummy nibh euismod tincid</p>
</section>

<!-- 9 values with portrait -->
<section class="slide c3 r3">
  <div class="brand"><i></i>Tidewell</div>
  <div class="abs" style="left:0;top:10px;width:2px;height:20px;background:var(--pink)"></div>
  <h2 class="title" style="top:9px;line-height:1.2">Text<br>Added<br>Here</h2>
  <div class="rule" style="top:44px"></div>
  <p class="fill abs" style="left:11px;top:51px;width:40px">Our team walks beside each woman from the first visit to the last check, with care and calm.<br><br>Every plan is built around her needs and her pace.</p>
  <div class="abs" style="left:56px;top:0;width:83px;height:134px;background:var(--pink)"></div>
  <div class="photo" role="img" aria-label="Photo of a smiling young woman with hands on her chest" style="left:62px;top:6px;width:72px;height:128px;background:linear-gradient(170deg,#f0ddd7,#d9a896 35%,#9cb6cc 70%,#7f9db6)"></div>
  <div class="abs" style="left:130px;top:25px;width:18px;height:18px;background:var(--ink)"></div>
  <div class="abs" style="left:130px;top:60px;width:18px;height:18px;background:var(--ink)"></div>
  <div class="abs" style="left:130px;top:95px;width:18px;height:18px;background:var(--ink)"></div>
  <svg class="abs" style="left:130px;top:25px" width="18" height="88" viewBox="0 0 18 88" fill="#fff"><circle cx="9" cy="7" r="2.2"/><path d="M4 14 Q9 9 14 14Z"/><circle cx="6.5" cy="42" r="1.8"/><circle cx="11.5" cy="42" r="1.8"/><rect x="5" y="44.5" width="3" height="6"/><rect x="10" y="44.5" width="3" height="6"/><path d="M9 82 L5 78 A2 2 0 0 1 9 76 A2 2 0 0 1 13 78Z"/></svg>
  <div class="abs" style="left:152px;top:26px;width:80px"><p class="h-pink" style="font-size:4.2px;font-weight:700">We Before Me</p><p class="fill">Care centred on each patient, with time to listen and adapt</p></div>
  <div class="abs" style="left:152px;top:61px;width:80px"><p class="h-pink" style="font-size:4.2px;font-weight:700">We Are Good People</p><p class="fill">A warm and skilled team that works together at every step</p></div>
  <div class="abs" style="left:152px;top:96px;width:80px"><p class="h-pink" style="font-size:4.2px;font-weight:700">We Work with Heart</p><p class="fill">Gentle hands, clear words and steady support each week</p></div>
  <span class="page-no">8</span>
</section>

<!-- 10 statistics -->
<section class="slide c1 r4">
  <div class="brand"><i></i>Tidewell</div>
  <div class="abs" style="left:0;top:10px;width:2px;height:14px;background:var(--pink)"></div>
  <h2 class="title" style="left:14px;top:10px">Text<br>Added Here</h2>
  <div class="rule" style="left:14px;top:31px"></div>
  <p class="fill abs" style="left:14px;top:35px;width:125px">Figures below give a short view of how many patients the service has followed and supported through care.<br><br>Most return to full movement within months, with regular guided sessions and a clear home plan to follow.</p>
  <p class="abs" style="left:21px;top:76px;font:700 7.6px/1 Montserrat,sans-serif;color:var(--pink)">768K</p>
  <p class="abs" style="left:70px;top:76px;font:700 7.6px/1 Montserrat,sans-serif;color:var(--pink)">423K</p>
  <div class="abs" style="left:63px;top:76px;width:.4px;height:22px;background:#ccc"></div>
  <div class="abs" style="left:16px;top:86px;width:44px"><p class="h-ink" style="font-size:3.8px">Lorem Ipsum</p><p class="fill">Patients followed since the start</p></div>
  <div class="abs" style="left:70px;top:86px;width:44px"><p class="h-ink" style="font-size:3.8px">Lorem Ipsum</p><p class="fill">Sessions given in the last year</p></div>
  <div class="abs" style="left:151px;top:54px;width:86.5px;height:15px;background:var(--pink);color:#fff;font:600 5.4px/15px Montserrat,sans-serif;padding-left:6px">Lorem Dolor Sit</div>
  <div class="abs" style="left:124px;top:69px;width:113.5px;height:46px;background:var(--lavender)"></div>
  <div class="photo" role="img" aria-label="Photo of a therapist's hands massaging a scar on the torso" style="left:129px;top:69px;width:94px;height:46px;background:linear-gradient(100deg,#c7a18e,#d8b6a3 50%,#5a6f86)"></div>
  <div class="foot-mark"></div><div class="foot-line"></div><span class="page-no">9</span>
</section>

<!-- 11 hub with three projects -->
<section class="slide c2 r4">
  <div class="brand"><i></i>Tidewell</div>
  <h2 class="title">Text Added Here</h2><div class="rule"></div>
  <div class="abs" style="left:25px;top:40px;width:57px;height:57px;border-radius:50%;border:1.3px solid var(--pink);display:flex;align-items:center;justify-content:center"><div style="width:48px;height:48px;border-radius:50%;border:.5px solid var(--pink);display:flex;align-items:center;justify-content:center;font:600 5px/1 Montserrat,sans-serif;color:var(--pink)">Tidewell</div></div>
  <svg class="abs" style="left:0;top:0" width="237.5" height="134" fill="none" stroke="#1b1b1b" stroke-width=".5"><path d="M84 62 L96 48 H120"/><path d="M86 68 H120"/><path d="M84 74 L96 98 H120"/></svg>
  <div class="abs" style="left:120px;top:39px;width:18px;height:18px;border-radius:50%;background:var(--ink)"></div>
  <div class="abs" style="left:120px;top:59px;width:18px;height:18px;border-radius:50%;background:var(--ink)"></div>
  <div class="abs" style="left:120px;top:89px;width:18px;height:18px;border-radius:50%;background:var(--ink)"></div>
  <svg class="abs" style="left:120px;top:39px" width="18" height="68" fill="none" stroke="#fff" stroke-width=".6"><circle cx="9" cy="9" r="4"/><circle cx="9" cy="9" r="2"/><circle cx="9" cy="29" r="4"/><circle cx="9" cy="29" r="2"/><circle cx="9" cy="59" r="4"/><circle cx="9" cy="59" r="2"/></svg>
  <div class="abs" style="left:142px;top:40px;width:88px"><p class="h-pink" style="font-weight:500">Project name</p><p class="fill">Short note on this project and how it helps patients in their daily care</p></div>
  <div class="abs" style="left:142px;top:60px;width:88px"><p class="h-pink" style="font-weight:500">Project name</p><p class="fill">Short note on this project and how it helps patients in their daily care</p></div>
  <div class="abs" style="left:142px;top:90px;width:88px"><p class="h-pink" style="font-weight:500">Project name</p><p class="fill">Short note on this project and how it helps patients in their daily care</p></div>
  <div class="foot-mark"></div><div class="foot-line"></div><span class="page-no">10</span>
</section>

<!-- 12 six column grid -->
<section class="slide c3 r4">
  <div class="brand"><i></i>Tidewell</div>
  <h2 class="title">Text Added Here</h2><div class="rule"></div>
  <div class="abs" style="left:17px;top:35px;width:62px"><p class="h-pink" style="font-size:3px;font-weight:500">1. Text Added Here</p><p class="fill" style="font-size:1.9px">Early movement of the arm helps restore reach and reduce stiffness after surgery. Small sets done each day matter most.</p></div>
  <div class="abs" style="left:89px;top:35px;width:62px"><p class="h-pink" style="font-size:3px;font-weight:500">1. Text Added Here</p><p class="fill" style="font-size:1.9px">Breathing work eases chest tension and supports calm during long weeks of treatment and rest periods.</p></div>
  <div class="abs" style="left:158px;top:35px;width:62px"><p class="h-pink" style="font-size:3px;font-weight:500">1. Text Added Here</p><p class="fill" style="font-size:1.9px">Lymph care reduces swelling through light touch, gentle pressure and simple habits at home.</p></div>
  <div class="abs" style="left:17px;top:78px;width:62px"><p class="h-pink" style="font-size:3px;font-weight:500">1. Text Added Here</p><p class="fill" style="font-size:1.9px">Scar care keeps the skin supple and free to glide over the tissue below it as healing goes on.</p></div>
  <div class="abs" style="left:89px;top:78px;width:62px"><p class="h-pink" style="font-size:3px;font-weight:500">1. Text Added Here</p><p class="fill" style="font-size:1.9px">Strength work returns step by step, with loads set to energy levels and the advice of the doctor.</p></div>
  <div class="abs" style="left:158px;top:78px;width:62px"><p class="h-pink" style="font-size:3px;font-weight:500">1. Text Added Here</p><p class="fill" style="font-size:1.9px">Return to sport and work is planned together, with clear goals and regular checks of progress.</p></div>
  <div class="foot-mark"></div><div class="foot-line"></div><span class="page-no">11</span>
</section>

<!-- 13 banded feature -->
<section class="slide c1 r5">
  <div class="brand"><i></i>Tidewell</div>
  <h2 class="title">Text Added Here</h2><div class="rule"></div>
  <p class="abs center" style="left:0;top:28px;width:237.5px;font:500 5px/1 Montserrat,sans-serif">Text Added Here</p>
  <p class="fill abs center" style="left:26px;top:36px;width:186px;color:#555">Team meetings bring together surgeons, nurses and physiotherapists to share each patient's progress and plan next steps.<br><br>Clear shared notes keep everyone aligned and let the patient hear one calm, consistent message.</p>
  <div class="abs" style="left:21px;top:63px;width:63px;height:48px;background:var(--pink);padding:5px"><p style="font:600 5px/1.2 Montserrat,sans-serif;color:#fff">Text Here</p><p class="fill" style="color:#fff;font-size:2.1px">Short summary of the care team and the role it plays for each patient.</p></div>
  <div class="photo" role="img" aria-label="Photo of a team meeting around a conference table" style="left:84px;top:63px;width:70px;height:48px;background:linear-gradient(120deg,#d7dde3,#9aa6b3 50%,#5b6570)"></div>
  <div class="abs" style="left:154px;top:63px;width:63px;height:48px;background:var(--ink);padding:5px"><p style="font:600 5px/1.2 Montserrat,sans-serif;color:#fff">Text Here</p><p class="fill" style="color:#fff;font-size:2.1px">Short summary of the care team and the role it plays for each patient.</p></div>
  <div class="foot-mark"></div><div class="foot-line"></div><span class="page-no">12</span>
</section>

<!-- 14 what we have -->
<section class="slide c2 r5">
  <div class="brand"><i></i>Tidewell</div>
  <h2 class="title">Text Added Here</h2><div class="rule"></div>
  <div class="photo" role="img" aria-label="Clinical photos of four healed breast surgery cases" style="left:22px;top:55px;width:191px;height:58px;background:linear-gradient(90deg,#c9a092,#d7b0a2 25%,#fff 25.3%,#fff 26%,#d6aa9a 26%,#c29484 52%,#fff 52.3%,#fff 53%,#cfa292 53%,#c99888 70%,#fff 70.3%,#fff 71%,#d9b2a3 71%,#caa093)"></div>
  <div class="abs" style="left:26px;top:31px;width:48px;height:30px;background:var(--pink)"></div>
  <p class="abs serif center" style="left:26px;top:33px;width:48px;font-weight:900;font-size:7px;line-height:1.1;color:var(--ink)">What<br>We<br>Have</p>
  <div class="abs" style="left:87px;top:35px;width:55px"><p class="h-pink" style="font-size:3.2px;font-weight:500">1. Lorem Ipsum</p><p class="fill">Brief note on results seen after surgery and care</p></div>
  <div class="abs" style="left:150px;top:35px;width:55px"><p class="h-pink" style="font-size:3.2px;font-weight:500">2. Lorem Ipsum</p><p class="fill">Brief note on results seen after surgery and care</p></div>
  <div class="foot-mark"></div><div class="foot-line"></div><span class="page-no">13</span>
</section>

<!-- 15 photo with steps -->
<section class="slide c3 r5">
  <div class="brand"><i></i>Tidewell</div>
  <h2 class="title">Text Added Here</h2><div class="rule"></div>
  <div class="photo" role="img" aria-label="Clinical photo of a patient after breast reconstruction" style="left:22px;top:30px;width:69px;height:81px;background:linear-gradient(160deg,#7b4f48,#d2a08d 40%,#c89180 70%,#8e5e52)"></div>
  <div class="abs" style="left:95px;top:30px;width:.4px;height:81px;background:#ddd"></div>
  <div class="dot-num" style="left:108px;top:38px">1</div>
  <div class="dot-num" style="left:108px;top:66px">2</div>
  <div class="dot-num" style="left:108px;top:95px">3</div>
  <p class="fill abs" style="left:124px;top:38px;width:104px">Check the chest wall and shoulder range at each visit and note any change in comfort or reach.</p>
  <p class="fill abs" style="left:124px;top:66px;width:104px">Assess the scar for tension or pulling and plan gentle skin work for the weeks ahead.<br>Note any swelling of the arm and agree on simple habits to limit it at home.</p>
  <p class="fill abs" style="left:124px;top:95px;width:104px">Review the goals set together and adjust the plan to match energy and mood.</p>
  <div class="foot-mark"></div><div class="foot-line"></div><span class="page-no">14</span>
</section>

<!-- 16 big statement -->
<section class="slide c1 r6">
  <div class="brand"><i></i>Tidewell</div>
  <div class="abs" style="left:0;top:8px;width:49px;height:10px;background:var(--pink)"></div>
  <div class="abs" style="left:0;top:8px;width:11px;height:117px;background:var(--pink)"></div>
  <div class="photo" role="img" aria-label="Clinical photo of a mastectomy scar" style="left:11px;top:18px;width:64px;height:91px;background:linear-gradient(160deg,#caa79b,#c29a8c 50%,#8a6a60)"></div>
  <div class="photo" role="img" aria-label="Clinical photo of a reconstructed breast" style="left:80px;top:18px;width:63px;height:91px;background:linear-gradient(200deg,#6f5a52,#d9b6a4 40%,#e4c6b6)"></div>
  <p class="abs serif" style="left:154px;top:40px;font-weight:900;font-size:15px;line-height:1.2">Text<br><span style="color:var(--pink)">Added</span><br>Here</p>
  <div class="foot-mark"></div><div class="foot-line"></div><span class="page-no">15</span>
</section>

<!-- 17 illustration with text -->
<section class="slide c2 r6">
  <div class="brand"><i></i>Tidewell</div>
  <div class="photo" role="img" aria-label="Line illustration of a hand holding a young plant" style="left:0;top:23px;width:93px;height:103px;background:radial-gradient(ellipse at 45% 55%,#ecdbea,#fff 72%)"></div>
  <div class="abs" style="left:108px;top:27px;width:115px">
    <p class="h-pink" style="font-weight:500;font-size:4px">1. Text Added Here</p>
    <p class="fill" style="color:#555;text-align:justify">Small daily steps build a strong base for recovery. Gentle moves of the arm and shoulder, done often, keep the joint free and the skin soft as the weeks go by.<br><br>Patients learn to read their body and to pace effort with rest and calm breathing.</p>
    <p class="h-pink" style="font-weight:500;font-size:4px;margin-top:6px">1. Text Added Here</p>
    <p class="fill" style="color:#555;text-align:justify">Growth takes time. Each session adds a little range, a little strength and a little more trust, until daily life feels familiar again.<br><br>Follow-up visits keep the plan on track and catch early signs that need attention.</p>
  </div>
  <div class="foot-mark"></div><div class="foot-line"></div><span class="page-no">16</span>
</section>

<!-- 18 three options -->
<section class="slide c3 r6">
  <div class="brand"><i></i>Tidewell</div>
  <h2 class="title">Text Added Here</h2><div class="rule"></div>
  <svg class="abs" style="left:14px;top:55px" width="24" height="26"><path d="M2 0 H10 L22 13 L10 26 H2 L14 13Z" fill="#e4e4e6"/></svg>
  <div class="photo" role="img" aria-label="Clinical photo of a first surgical option" style="left:60px;top:28px;width:45px;height:53px;background:linear-gradient(170deg,#caa094,#d6b0a2 60%,#b28c82)"></div>
  <div class="photo" role="img" aria-label="Clinical photo of a second surgical option" style="left:118px;top:28px;width:45px;height:53px;background:linear-gradient(170deg,#b08e84,#d4a99a 60%,#c99b8b)"></div>
  <div class="photo" role="img" aria-label="Clinical photo of a third surgical option" style="left:176px;top:28px;width:45px;height:53px;background:linear-gradient(170deg,#c3a79b,#d0a595 60%,#ad857a)"></div>
  <div class="abs" style="left:60px;top:85px;width:45px"><p class="h-ink" style="font-size:3.6px;font-weight:600"><span style="color:var(--pink)">First</span> Option</p><p class="fill">Short note on this approach and when it is chosen for care</p></div>
  <div class="abs" style="left:118px;top:85px;width:45px"><p class="h-ink" style="font-size:3.6px;font-weight:600"><span style="color:var(--pink)">Second</span> Option</p><p class="fill">Short note on this approach and when it is chosen for care</p></div>
  <div class="abs" style="left:176px;top:85px;width:45px"><p class="h-ink" style="font-size:3.6px;font-weight:600"><span style="color:var(--pink)">Third</span> Option</p><p class="fill">Short note on this approach and when it is chosen for care</p></div>
  <div class="foot-mark"></div><div class="foot-line"></div><span class="page-no">17</span>
</section>

<!-- 19 timeline -->
<section class="slide c1 r7">
  <div class="brand"><i></i>Tidewell</div>
  <h2 class="title">Text Added Here</h2><div class="rule"></div>
  <svg class="abs" style="left:0;top:0" width="237.5" height="134">
    <g fill="#d9749a"><path d="M21 68 H57 L60 72 L57 76 H21 L24 72Z"/><path d="M98 68 H134 L137 72 L134 76 H98 L101 72Z"/><path d="M175 68 H214 L217 72 L214 76 H175 L178 72Z"/></g>
    <g fill="#1b1b1b"><path d="M60 68 H95 L98 72 L95 76 H60 L63 72Z"/><path d="M137 68 H172 L175 72 L172 76 H137 L140 72Z"/></g>
    <g stroke="#d9749a" stroke-width=".6"><line x1="42" y1="54" x2="42" y2="66"/><line x1="118" y1="54" x2="118" y2="66"/><line x1="196" y1="54" x2="196" y2="66"/></g>
    <g fill="#d9749a"><circle cx="42" cy="54" r="1.5"/><circle cx="118" cy="54" r="1.5"/><circle cx="196" cy="54" r="1.5"/></g>
    <g stroke="#1b1b1b" stroke-width=".6"><line x1="80" y1="78" x2="80" y2="90"/><line x1="157" y1="78" x2="157" y2="90"/></g>
    <g fill="#1b1b1b"><circle cx="80" cy="90" r="1.5"/><circle cx="157" cy="90" r="1.5"/></g>
    <g font-family="Montserrat,sans-serif" font-size="3.2" font-weight="600" fill="#fff" text-anchor="middle"><text x="40" y="73.2">1990</text><text x="79" y="73.2">2001</text><text x="118" y="73.2">2007</text><text x="156" y="73.2">2012</text><text x="196" y="73.2">2020</text></g>
  </svg>
  <div class="abs center" style="left:22px;top:40px;width:40px"><p class="h-pink" style="font-size:3.2px;font-weight:500">Your Title</p><p class="fill">Refers to a good or service being offered</p></div>
  <div class="abs center" style="left:98px;top:40px;width:40px"><p class="h-pink" style="font-size:3.2px;font-weight:500">Your Title</p><p class="fill">Refers to a good or service being offered</p></div>
  <div class="abs center" style="left:176px;top:40px;width:40px"><p class="h-pink" style="font-size:3.2px;font-weight:500">Your Title</p><p class="fill">Refers to a good or service being offered</p></div>
  <div class="abs center" style="left:60px;top:94px;width:40px"><p class="h-ink" style="font-size:3.2px;font-weight:600">Your Title</p><p class="fill">Refers to a good or service being offered</p></div>
  <div class="abs center" style="left:137px;top:94px;width:40px"><p class="h-ink" style="font-size:3.2px;font-weight:600">Your Title</p><p class="fill">Refers to a good or service being offered</p></div>
  <div class="foot-mark"></div><div class="foot-line"></div><span class="page-no">18</span>
</section>

<!-- 20 cycle -->
<section class="slide c2 r7">
  <div class="brand"><i></i>Tidewell</div>
  <h2 class="title">Text Added Here</h2><div class="rule"></div>
  <svg class="abs" style="left:87px;top:40px" width="66" height="66" viewBox="0 0 66 66">
    <path d="M33 0 A33 33 0 0 1 66 33 H48 A15 15 0 0 0 33 18Z" fill="#d9749a"/>
    <path d="M66 33 A33 33 0 0 1 33 66 V48 A15 15 0 0 0 48 33Z" fill="#1b1b1b"/>
    <path d="M33 66 A33 33 0 0 1 0 33 H18 A15 15 0 0 0 33 48Z" fill="#d9749a"/>
    <path d="M0 33 A33 33 0 0 1 33 0 V18 A15 15 0 0 0 18 33Z" fill="#1b1b1b"/>
    <g stroke="#fff" stroke-width=".9" fill="none"><line x1="33" y1="0" x2="33" y2="18"/><line x1="48" y1="33" x2="66" y2="33"/><line x1="33" y1="48" x2="33" y2="66"/><line x1="0" y1="33" x2="18" y2="33"/>
    <circle cx="17" cy="17" r="3"/><circle cx="49" cy="17" r="3"/><circle cx="49" cy="49" r="3"/><circle cx="17" cy="49" r="3"/></g>
    <text x="33" y="32" font-family="Montserrat,sans-serif" font-weight="700" font-size="5.2" text-anchor="middle" fill="#1b1b1b">Text</text>
    <text x="33" y="38.5" font-family="Montserrat,sans-serif" font-weight="700" font-size="5.2" text-anchor="middle" fill="#1b1b1b">Added</text>
  </svg>
  <div class="abs" style="left:25px;top:42px;width:56px;text-align:right"><p class="h-ink" style="font-size:3.4px;font-weight:600">Text Here</p><p class="fill">Short note on this stage of the care cycle</p></div>
  <div class="abs" style="left:25px;top:89px;width:56px;text-align:right"><p class="h-pink" style="font-size:3.4px;font-weight:600">Text Here</p><p class="fill">Short note on this stage of the care cycle</p></div>
  <div class="abs" style="left:159px;top:42px;width:56px"><p class="h-pink" style="font-size:3.4px;font-weight:600">Text Here</p><p class="fill">Short note on this stage of the care cycle</p></div>
  <div class="abs" style="left:159px;top:89px;width:56px"><p class="h-ink" style="font-size:3.4px;font-weight:600">Text Here</p><p class="fill">Short note on this stage of the care cycle</p></div>
  <div class="foot-mark"></div><div class="foot-line"></div><span class="page-no">19</span>
</section>

<!-- 21 steps -->
<section class="slide c3 r7">
  <div class="brand"><i></i>Tidewell</div>
  <h2 class="title">Text Added Here</h2><div class="rule"></div>
  <svg class="abs" style="left:29px;top:47px" width="182" height="21" viewBox="0 0 182 21">
    <path d="M0 0 H32 L38 10.5 L32 21 H0 L6 10.5Z" fill="#d9749a"/>
    <path d="M35 0 H67 L73 10.5 L67 21 H35 L41 10.5Z" fill="#1b1b1b"/>
    <path d="M70 0 H102 L108 10.5 L102 21 H70 L76 10.5Z" fill="#d9749a"/>
    <path d="M105 0 H137 L143 10.5 L137 21 H105 L111 10.5Z" fill="#1b1b1b"/>
    <path d="M140 0 H172 L178 10.5 L172 21 H140 L146 10.5Z" fill="#d9749a"/>
    <g font-family="Montserrat,sans-serif" font-size="3.4" font-weight="600" fill="#fff" text-anchor="middle"><text x="20" y="11.7">STEP 01</text><text x="55" y="11.7">STEP 02</text><text x="90" y="11.7">STEP 03</text><text x="125" y="11.7">STEP 04</text><text x="160" y="11.7">STEP 05</text></g>
  </svg>
  <div class="abs center" style="left:31px;top:76px;width:32px"><p class="h-ink" style="font-size:3px;font-weight:600">Project name</p><p class="fill" style="font-size:2px">Short text on this step of the plan and its aim</p></div>
  <div class="abs center" style="left:66px;top:76px;width:32px"><p class="h-pink" style="font-size:3px;font-weight:500">Project name</p><p class="fill" style="font-size:2px">Short text on this step of the plan and its aim</p></div>
  <div class="abs center" style="left:101px;top:76px;width:32px"><p class="h-ink" style="font-size:3px;font-weight:600">Project name</p><p class="fill" style="font-size:2px">Short text on this step of the plan and its aim</p></div>
  <div class="abs center" style="left:136px;top:76px;width:32px"><p class="h-pink" style="font-size:3px;font-weight:500">Project name</p><p class="fill" style="font-size:2px">Short text on this step of the plan and its aim</p></div>
  <div class="abs center" style="left:171px;top:76px;width:32px"><p class="h-ink" style="font-size:3px;font-weight:600">Project name</p><p class="fill" style="font-size:2px">Short text on this step of the plan and its aim</p></div>
  <div class="foot-mark"></div><div class="foot-line"></div><span class="page-no">20</span>
</section>

<!-- 22 the ask -->
<section class="slide c1 r8">
  <div class="brand"><i></i>Tidewell</div>
  <h2 class="title">Text Added Here</h2><div class="rule"></div>
  <p class="abs" style="left:13px;top:44px;font:500 12px/1 Montserrat,sans-serif">The <span style="color:var(--pink);font-weight:700">Ask.</span></p>
  <div class="abs" style="left:23px;top:64px;width:3.5px;height:3.5px;border-radius:50%;background:var(--pink)"></div>
  <div class="abs" style="left:31px;top:63px;width:60px"><p class="h-ink" style="font-size:3.8px;font-weight:600">Lorem ipsum</p><p class="fill">What we ask of partners to help more patients reach good care</p></div>
  <div class="abs" style="left:23px;top:86px;width:3.5px;height:3.5px;border-radius:50%;background:var(--pink)"></div>
  <div class="abs" style="left:31px;top:85px;width:60px"><p class="h-ink" style="font-size:3.8px;font-weight:600">Lorem ipsum</p><p class="fill">What we ask of partners to help more patients reach good care</p></div>
  <div class="abs" style="left:107px;top:23px;width:102px;height:68px;background:var(--ink);border-radius:2px;padding:3px">
    <div style="position:relative;width:100%;height:100%;background:#fff;overflow:hidden">
      <p style="position:absolute;left:6px;top:6px;font:600 3px/1 Montserrat,sans-serif;color:var(--pink)">Tidewell Physio</p>
      <p style="position:absolute;left:6px;top:22px;width:44px;font:700 3.6px/1.15 Montserrat,sans-serif;color:var(--pink)">Along the Quiet Shore of <span style="color:var(--ink)">Healing Days</span></p>
      <div role="img" aria-label="Photo of a woman holding a pink ribbon" style="position:absolute;left:55px;top:4px;width:36px;height:48px;background:linear-gradient(160deg,#efe9ea,#d06a8e)"></div>
    </div>
  </div>
  <div class="abs" style="left:107px;top:91px;width:102px;height:6px;background:#d2d3d6"></div>
  <div class="abs" style="left:150px;top:97px;width:16px;height:7px;background:#bfc0c3"></div>
  <div class="abs" style="left:142px;top:104px;width:32px;height:2px;background:#aeafb2;border-radius:1px"></div>
  <div class="abs" style="left:170px;top:83px;width:51px;height:8px;background:var(--pink);color:#fff;font:600 3.6px/8px Montserrat,sans-serif;text-align:center">Text Added Here</div>
  <div class="foot-mark"></div><div class="foot-line"></div><span class="page-no">21</span>
</section>

<!-- 23 team -->
<section class="slide c2 r8">
  <div class="brand"><i></i>Tidewell</div>
  <h2 class="title">Text Added Here</h2><div class="rule"></div>
  <div class="abs" style="left:22px;top:45px;width:35px;height:13px;background:var(--ink)"></div>
  <div class="abs" style="left:74px;top:45px;width:35px;height:13px;background:var(--pink)"></div>
  <div class="abs" style="left:127px;top:45px;width:35px;height:13px;background:var(--ink)"></div>
  <div class="abs" style="left:181px;top:45px;width:35px;height:13px;background:var(--pink)"></div>
  <div class="photo" role="img" aria-label="Portrait photo of team member" style="left:30px;top:47px;width:19px;height:19px;border-radius:50%;border:1px solid #fff;background:#c9b2a6"></div>
  <div class="photo" role="img" aria-label="Portrait photo of team member" style="left:82px;top:47px;width:19px;height:19px;border-radius:50%;border:1px solid #fff;background:#8f735f"></div>
  <div class="photo" role="img" aria-label="Portrait photo of team member" style="left:135px;top:47px;width:19px;height:19px;border-radius:50%;border:1px solid #fff;background:#c9b2a6"></div>
  <div class="photo" role="img" aria-label="Portrait photo of team member" style="left:189px;top:47px;width:19px;height:19px;border-radius:50%;border:1px solid #fff;background:#8f735f"></div>
  <div class="abs center" style="left:18px;top:73px;width:43px"><p class="h-pink" style="font-size:3.4px;font-weight:600">JOHN SMITH</p><p class="fill" style="font-size:1.9px">Surgeon who leads the care plan and follows each case closely</p></div>
  <div class="abs center" style="left:70px;top:73px;width:43px"><p class="h-ink" style="font-size:3.4px;font-weight:700">MILLIE SMITH</p><p class="fill" style="font-size:1.9px">Nurse who guides patients through each stage of treatment</p></div>
  <div class="abs center" style="left:123px;top:73px;width:43px"><p class="h-pink" style="font-size:3.4px;font-weight:600">JOHN SMITH</p><p class="fill" style="font-size:1.9px">Physiotherapist in charge of scar care and movement</p></div>
  <div class="abs center" style="left:177px;top:73px;width:43px"><p class="h-ink" style="font-size:3.4px;font-weight:700">MILLIE SMITH</p><p class="fill" style="font-size:1.9px">Counsellor who supports mood, body image and return to life</p></div>
  <div class="foot-mark"></div><div class="foot-line"></div><span class="page-no">19</span>
</section>

<!-- 24 thank you -->
<section class="slide c3 r8">
  <div class="abs" style="left:0;top:0;width:60px;height:134px;background:var(--pink)"></div>
  <div class="abs" style="left:72px;top:40px;width:12px;height:12px;background:var(--pink)"></div>
  <p class="abs" style="left:72px;top:58px;width:60px;font:700 8px/1.15 Montserrat,sans-serif;color:var(--pink)">Tidewell<br>Physio</p>
  <p class="abs" style="left:141px;top:38px;font:900 14.5px/1 Montserrat,sans-serif">Thank You</p>
  <svg class="abs" style="left:142px;top:60px" width="8" height="40" fill="#d9749a"><path d="M1 1 Q1 7 7 7 L7 5 L5 4 L4 5 Q2 4 3 3 L4 2 L3 0Z"/><path d="M1 15 L7 18 L1 21 L2 18Z"/><path d="M4 29 L7 32 H6 V35 H2 V32 H1Z"/></svg>
  <div class="abs" style="left:152px;top:60px;width:.4px;height:8px;background:#999"></div>
  <div class="abs" style="left:152px;top:75px;width:.4px;height:8px;background:#999"></div>
  <div class="abs" style="left:152px;top:89px;width:.4px;height:8px;background:#999"></div>
  <p class="fill abs" style="left:155px;top:60px;color:#444;font-size:2.7px">+18 2767 9470 1808<br>+18 2767 9470 1808</p>
  <p class="fill abs" style="left:155px;top:75px;color:#444;font-size:2.7px">www.websitename.com<br>urname@email.com</p>
  <p class="fill abs" style="left:155px;top:89px;color:#444;font-size:2.7px">1234 Street name, town/city,<br>state/country, post/zip 012345.</p>
</section>

</body>
</html>
```